The billboard should communicate confidence, energy and approachability while maintaining a professional, premium feel. Rather than relying on a standard agent photograph, property collage or crowded list of services, we would like an original creative idea that makes people look twice. This could involve a fun visual, clever headline, striking colour contrast or an unexpected real estate theme. The concept should feel positive and contemporary, with enough personality to become recognisable throughout the local community.

The key message should appeal to homeowners who are thinking about selling, preparing to sell or simply curious about the value of their property. Copy must be short, clear and conversational, supported by a direct call to action. The agent’s name, phone number and company branding should remain highly visible without competing with the main idea.

The finished billboard will measure 8.0 metres wide by 2.08 metres high (1224px x 324px), so the composition must suit a long landscape format. All important text and imagery should remain comfortably within safe margins and be legible from a distance. The design should avoid small writing, unnecessary detail and visual clutter.

The goal is to create a billboard that feels different from every other real estate sign in the area—something engaging, confident and easy to remember. It should build strong brand awareness, generate conversations and encourage local property owners to contact the agent when they are ready to make their next move. The concept should be adaptable for future campaigns, helping establish a consistent, distinctive and trusted local brand presence.

Target Market(s)

ages 30+

Industry/Entity Type

Real Estate

Requirements
Must have
• call Colin and phone number 0437 15 82 63
Nice to have
• Nice bright and yellow.. Exciting and grabbing

```html
<!DOCTYPE html>
<html lang="en">
<head>
<meta charset="utf-8">
<title>Sell your Property – Billboard</title>
<link href="https://fonts.googleapis.com/css2?family=Source+Sans+3:wght@700;900&display=swap" rel="stylesheet">
<style>
  :root {
    --orange: #f7a600;
    --orange-deep: #f29a00;
    --olive: #8f9a1e;
    --olive-light: #b8b43a;
    --sun: #ffe89a;
    --ink: #000000;
    --paper: #ffffff;
    --phone: #f7a300;
  }
  html, body {
    margin: 0;
    padding: 0;
    width: 1200px;
    height: 318px;
    overflow: hidden;
    background: var(--orange);
  }
  .billboard {
    display: block;
    width: 1200px;
    height: 318px;
    font-family: "Source Sans 3", Arial, sans-serif;
  }
  .headline {
    font-weight: 900;
    font-size: 74px;
    fill: var(--ink);
    stroke: var(--paper);
    stroke-width: 5px;
    paint-order: stroke;
    filter: drop-shadow(3px 4px 1px rgba(0,0,0,.55));
  }
  .pitch, .we-label, .call-label {
    font-weight: 900;
    font-size: 56px;
    fill: var(--paper);
    stroke: var(--ink);
    stroke-width: 3px;
    paint-order: stroke;
    filter: drop-shadow(3px 3px 1px rgba(0,0,0,.6));
  }
  .phone-number {
    font-weight: 900;
    font-size: 56px;
    fill: var(--phone);
    stroke: var(--ink);
    stroke-width: 4px;
    paint-order: stroke;
    filter: drop-shadow(3px 3px 1px rgba(0,0,0,.6));
  }
  .service-tag { fill: var(--ink); }
  .service-text {
    font-weight: 700;
    font-size: 36px;
    fill: var(--paper);
    stroke: var(--ink);
    stroke-width: 2px;
    paint-order: stroke;
    filter: drop-shadow(2px 2px 1px rgba(0,0,0,.6));
  }
  .brand-name {
    font-weight: 900;
    font-size: 44px;
    fill: var(--ink);
  }
</style>
</head>
<body>
<svg class="billboard" viewBox="0 0 1200 318" xmlns="http://www.w3.org/2000/svg">
  <defs>
    <linearGradient id="scene-tone" x1="0" y1="0" x2="1" y2="1">
      <stop offset="0" stop-color="#d9b02a"/>
      <stop offset=".45" stop-color="var(--olive-light)"/>
      <stop offset="1" stop-color="var(--olive)"/>
    </linearGradient>
    <radialGradient id="sun-glow" cx="1" cy=".15" r=".7">
      <stop offset="0" stop-color="var(--sun)"/>
      <stop offset="1" stop-color="var(--sun)" stop-opacity="0"/>
    </radialGradient>
    <linearGradient id="warm-field" x1="0" y1="0" x2="0" y2="1">
      <stop offset="0" stop-color="var(--orange)"/>
      <stop offset="1" stop-color="var(--orange-deep)"/>
    </linearGradient>
  </defs>

  <rect class="backdrop" width="1200" height="318" fill="url(#warm-field)"/>
  <g class="scene" role="img" aria-label="Sunburst over a city skyline and green suburban landscape">
    <polygon points="430,0 1200,0 1200,318 535,318" fill="url(#scene-tone)"/>
    <polygon points="430,0 1200,0 1200,318 535,318" fill="url(#sun-glow)"/>
  </g>

  <text class="headline" x="40" y="89" textLength="1123" lengthAdjust="spacingAndGlyphs">Do You want to Sell your Property?</text>

  <g class="brand-name-block">
    <text class="brand-name" x="44" y="190">Dale</text>
    <text class="brand-name" x="44" y="238">Forsyth</text>
  </g>

  <g class="pitch-block">
    <text class="pitch" x="211" y="165" textLength="224" lengthAdjust="spacingAndGlyphs">!!Sell Fast</text>
    <text class="pitch" x="211" y="219" textLength="228" lengthAdjust="spacingAndGlyphs">and at the</text>
    <text class="pitch" x="211" y="273" textLength="264" lengthAdjust="spacingAndGlyphs">Best Value¡¡</text>
  </g>

  <text class="we-label" x="551" y="165">We:</text>

  <g class="services">
    <polygon class="service-tag" points="656,127 744,127 744,216 700,229 656,216"/>
    <text class="service-text" x="669" y="162">Sell</text>

    <polygon class="service-tag" points="779,127 866,127 866,216 822,229 779,216"/>
    <text class="service-text" x="794" y="162" textLength="131" lengthAdjust="spacingAndGlyphs">Prepare</text>
    <text class="service-text" x="794" y="200" textLength="133" lengthAdjust="spacingAndGlyphs">the Sale</text>

    <polygon class="service-tag" points="958,127 1046,127 1046,216 1002,229 958,216"/>
    <text class="service-text" x="972" y="162" textLength="176" lengthAdjust="spacingAndGlyphs">Value your</text>
    <text class="service-text" x="972" y="200" textLength="146" lengthAdjust="spacingAndGlyphs">property</text>
  </g>

  <g class="call-to-action">
    <text class="call-label" x="551" y="273" textLength="206" lengthAdjust="spacingAndGlyphs">Call Colin:</text>
    <text class="phone-number" x="769" y="273" textLength="299" lengthAdjust="spacingAndGlyphs">0437 15 82 63</text>
  </g>
</svg>
</body>
</html>
```